(2) Trifold Brochures needed for automation industry

Need “Two” Trifold brochures. (files included) please see READ ME word doc attached.
1# will be for Pharmaceutical and Biotech companies. (stock photos and copy should be ALL pharma and biotech related.
#2 will be for food and beverage processing, Packaging & Distribution Center, Automotive, Chemical, Consumer Electronics, Government, Pulp & paper, Oil/Gas, Security & Detention, Water & Wastewater
Target Market(s)
automation industry - USA and Canada
Font styles to use
Serif
Requirements
Must have
- Target audience appeal. See attached Word file for ideas and details.
Nice to have
- Best looking Trifold Brochures in the industry
Should not have
- Cheap look

```html
<!DOCTYPE html>
<html lang="en">
<head>
<meta charset="utf-8">
<title>Veltrane Automation – Trifold Brochure</title>
<link href="https://fonts.googleapis.com/css2?family=Bebas+Neue&family=Montserrat:wght@400;600;700&display=swap" rel="stylesheet">
<style>
  :root {
    --navy: #2b2f8c;
    --navy-deep: #1f2270;
    --teal: #2aa6b5;
    --sky: #a6dbe6;
    --ink: #1c1c24;
    --mist: #eceef4;
    --paper: #ffffff;
    --notch: #b9bcc6;
    --stage: #d6d6d8;
  }
  * { box-sizing: border-box; margin: 0; padding: 0; }
  html, body { width: 1200px; height: 745px; overflow: hidden; }
  body { background: var(--stage); font-family: "Montserrat", Arial, sans-serif; color: var(--ink); position: relative; }

  .spread { position: absolute; left: 40px; top: 60px; width: 810px; height: 625px; display: flex; box-shadow: 0 10px 30px rgba(0,0,0,.18); }
  .panel { position: relative; width: 270px; height: 625px; overflow: hidden; background: var(--paper); }
  .panel + .panel { border-left: 1px solid #e2e3ea; }

  .icon-badge { position: absolute; left: 50%; width: 70px; height: 70px; margin-left: -35px; border-radius: 50%; display: flex; align-items: center; justify-content: center; }
  .icon-badge--navy { background: var(--navy); }
  .icon-badge--teal { background: var(--teal); }
  .icon-badge--sky { background: var(--sky); }

  .section-title { position: absolute; left: 0; right: 0; text-align: center; font-family: "Bebas Neue", "Oswald", sans-serif; font-size: 30px; letter-spacing: .5px; color: var(--navy); line-height: 1; }
  .section-title::after { content: ""; display: block; width: 96px; height: 1px; background: var(--navy); margin: 4px auto 0; }

  .about-copy { position: absolute; left: 30px; right: 22px; top: 168px; font-size: 13px; line-height: 1.55; }
  .about-copy strong { font-weight: 700; }

  .photo { position: absolute; left: 0; right: 0; }
  .photo--bottles { top: 300px; height: 240px; background: linear-gradient(160deg, #c9ccdc 0%, #eef0f6 45%, #8a4a26 78%, #5a2c14 100%); }
  .photo--worker { top: 0; height: 300px; background: linear-gradient(135deg, #2e3a6e 0%, #6f7fa8 40%, #e6b820 55%, #2b3460 100%); }
  .photo--cleanroom { top: 452px; height: 173px; background: linear-gradient(180deg, #f2f4f8 0%, #d9dde8 60%, #b9c2d4 100%); }
  .photo--reactor { top: 40px; height: 500px; background: linear-gradient(160deg, #e8e9ee 0%, #a9adb8 35%, #7c808c 60%, #c6c8cf 100%); }

  .band { position: absolute; left: 0; width: 100%; display: block; }

  .serve-body { position: absolute; left: 0; right: 0; top: 300px; bottom: 0; background: linear-gradient(180deg, #e9ebf2 0%, #f7f8fb 100%); }
  .bullet-list { position: absolute; list-style: none; font-size: 11px; line-height: 1.55; }
  .bullet-list li::before { content: "•"; margin-right: 7px; }
  .bullet-list--serve { left: 42px; top: 388px; }

  .service-list { position: absolute; left: 46px; top: 162px; font-size: 11px; line-height: 1.5; }
  .service-list .group { font-weight: 700; margin-top: 2px; }
  .service-list ul { list-style: none; padding-left: 10px; }
  .service-list ul li::before { content: "•"; margin-right: 7px; }

  .cover { position: absolute; left: 890px; top: 60px; width: 270px; height: 625px; background: var(--paper); overflow: hidden; box-shadow: 0 10px 30px rgba(0,0,0,.18); }
  .cover-banner { position: absolute; left: -10px; top: 232px; width: 290px; height: 112px; }
  .cover-headline { position: absolute; left: 0; right: 0; top: 250px; text-align: center; font-family: "Bebas Neue", "Oswald", sans-serif; font-weight: 400; color: var(--paper); font-size: 40px; line-height: .95; transform: skewX(-10deg); letter-spacing: .5px; }
  .cover-headline span { display: block; }
  .cover-headline .line-two { font-size: 46px; }

  .brand { position: absolute; left: 0; right: 0; top: 570px; display: flex; align-items: center; justify-content: center; gap: 8px; }
  .brand-mark { width: 14px; height: 14px; border-radius: 50%; background: var(--navy); }
  .brand-name { font-family: "Montserrat", Arial, sans-serif; font-weight: 700; font-size: 14px; letter-spacing: 1.5px; color: var(--navy); }
</style>
</head>
<body>

<section class="spread" aria-label="Inside spread">
  <article class="panel panel--about">
    <div class="icon-badge icon-badge--navy" style="top:40px">
      <svg width="40" height="40" viewBox="0 0 40 40" aria-hidden="true">
        <circle cx="20" cy="20" r="10" fill="none" stroke="#ffffff" stroke-width="3"/>
        <g stroke="#ffffff" stroke-width="4" stroke-linecap="round">
          <line x1="20" y1="4" x2="20" y2="8"/><line x1="20" y1="32" x2="20" y2="36"/>
          <line x1="4" y1="20" x2="8" y2="20"/><line x1="32" y1="20" x2="36" y2="20"/>
          <line x1="8.7" y1="8.7" x2="11.5" y2="11.5"/><line x1="28.5" y1="28.5" x2="31.3" y2="31.3"/>
          <line x1="8.7" y1="31.3" x2="11.5" y2="28.5"/><line x1="28.5" y1="11.5" x2="31.3" y2="8.7"/>
        </g>
        <circle cx="20" cy="20" r="5" fill="none" stroke="#7fd6e0" stroke-width="3"/>
      </svg>
    </div>
    <h2 class="section-title" style="top:122px">About Us</h2>
    <p class="about-copy"><strong>Veltrane Automation</strong> is the leader in the automation industry. We are committed to providing exceptional service and cutting-edge technologies.</p>
    <div class="photo photo--bottles" role="img" aria-label="Filling machine nozzles over a line of amber glass bottles"></div>
    <svg class="band" style="top:540px" width="270" height="85" viewBox="0 0 270 85" aria-hidden="true">
      <rect width="270" height="85" fill="var(--mist)"/>
      <polygon points="0,0 270,0 270,14 30,14 0,40" fill="var(--navy)"/>
    </svg>
  </article>

  <article class="panel panel--serve">
    <div class="photo photo--worker" role="img" aria-label="Technician in a hard hat checking a tablet among factory machinery"></div>
    <svg class="band" style="top:0" width="270" height="40" viewBox="0 0 270 40" aria-hidden="true">
      <polygon points="0,0 90,0 0,34" fill="var(--navy)"/>
    </svg>
    <div class="serve-body"></div>
    <div class="icon-badge icon-badge--teal" style="top:262px">
      <svg width="36" height="36" viewBox="0 0 36 36" aria-hidden="true">
        <circle cx="18" cy="12" r="7" fill="#ffffff"/>
        <path d="M6 32 C6 22 30 22 30 32 Z" fill="var(--navy)"/>
      </svg>
    </div>
    <h2 class="section-title" style="top:346px">Who We Serve</h2>
    <ul class="bullet-list bullet-list--serve">
      <li>Pharmaceutical &amp; Biotech</li>
      <li>Food and Beverage Processing</li>
      <li>Packaging &amp; Distribution Center</li>
      <li>Automotive</li>
      <li>Chemical</li>
      <li>Consumer Electronics</li>
      <li>Government</li>
      <li>Pulp &amp; Paper</li>
      <li>Oil/Gas</li>
      <li>Security &amp; Detention</li>
      <li>Water &amp; Wastewater</li>
    </ul>
  </article>

  <article class="panel panel--services">
    <div class="icon-badge icon-badge--sky" style="top:40px">
      <svg width="40" height="40" viewBox="0 0 40 40" aria-hidden="true">
        <g stroke-linecap="round">
          <line x1="10" y1="10" x2="30" y2="30" stroke="var(--navy)" stroke-width="4"/>
          <line x1="30" y1="10" x2="12" y2="28" stroke="var(--teal)" stroke-width="5"/>
          <line x1="12" y1="28" x2="8" y2="32" stroke="var(--navy)" stroke-width="3"/>
        </g>
        <circle cx="9" cy="9" r="4" fill="none" stroke="var(--navy)" stroke-width="3"/>
      </svg>
    </div>
    <h2 class="section-title" style="top:122px">Our Services</h2>
    <div class="service-list">
      <div class="group">Automation</div>
      <ul><li>Complete Automation</li><li>System Integration</li><li>Industrial Robotics</li></ul>
      <div class="group">Documentation</div>
      <ul><li>Validation Documentation</li><li>Project Documentation</li><li>Testing &amp; Qualification</li></ul>
      <div class="group">Engineering Services</div>
      <ul><li>Design</li><li>Project Management</li><li>Consultation</li></ul>
    </div>
    <div class="photo photo--cleanroom" role="img" aria-label="Bright clean room with control screens"></div>
    <svg class="band" style="top:432px" width="270" height="22" viewBox="0 0 270 22" aria-hidden="true">
      <polygon points="0,6 270,0 270,12 0,20" fill="var(--navy)"/>
    </svg>
  </article>
</section>

<section class="cover" aria-label="Front cover">
  <div class="photo photo--reactor" role="img" aria-label="Stainless steel process reactor with piping in a clean room"></div>
  <svg class="band" style="top:40px" width="270" height="24" viewBox="0 0 270 24" aria-hidden="true">
    <polygon points="0,6 185,0 195,24 0,24" fill="var(--notch)"/>
    <polygon points="185,0 270,0 270,3 195,24" fill="var(--paper)"/>
  </svg>
  <svg class="cover-banner" viewBox="0 0 290 112" aria-hidden="true">
    <polygon points="0,18 290,0 290,94 0,112" fill="var(--navy-deep)" opacity=".92"/>
  </svg>
  <h1 class="cover-headline"><span>Great Technology</span><span class="line-two">Best Services</span></h1>
  <svg class="band" style="top:532px" width="270" height="14" viewBox="0 0 270 14" aria-hidden="true">
    <polygon points="0,4 270,0 270,8 0,12" fill="var(--navy)"/>
  </svg>
  <div class="brand">
    <span class="brand-mark" aria-hidden="true"></span>
    <span class="brand-name">VELTRANE AUTOMATION</span>
  </div>
</section>

</body>
</html>
```